Collective strata website refresh brellowquay.net.au

Description:
This website is managed by the leadership of a group of buildings in Harlow Point. The area and the collective stratas are known as Brellow Quay. The current website is messy and very dated. For the new site, we'd like to focus on a clean, user friendly design. The majority of the content on this site will be text. Most pages will use a one-pager scrolling format.

Current Site:
The current site is brellowquay.net.au

This site is functionally very good, but has certain issues due to its age. We are generally quite happy with the functionality of the site, despite layout issues.

Users:

The users are those who currently live or are interested in living in Brellow quay. This group has a large demographic spread, notably including a large amount of older people. When designing remember people who may be less familiar with technology and the internet will make up many of the users of the site. 

Design:
This site should give a clean, professional and welcoming energy. It should be clean, simple and focused on efficiently displaying information to the user in an accessible and clear way.
As users typically come to the site looking for a specific piece of information or to use a service

We would like a navigation menu with the categories "Home, Services, Facilities, Stratas, About Us, Local Information, Contact”

For us to choose a winner, we would like you to design the home page, but the winner will be required to provide an example strata page (a page with some headings that link to articles below) and a standard page. They will also be required to provide all images used without charge.

If you are going to submit multiple designs or respond to feedback, please modify the menu and text layout between them. This is the most important part of the design, and multiple submissions with only minor aesthetic changes will be largely disregarded.

Requested:
Home Page

Winner to provide:
Strata Page
Standard page template

There are some photos you can use here:

https://www.trovik.net/temp/brellowquay.zip

It contains:
A couple of the boss's own photos
Some photos from a PDF pamphlet done by a large organisation you can use
The current logos

The boss has taken a couple of photos [sigh] so if there is a way in using them somewhere on the site please do. They are not critical to use.
You do not have to use any of the photos, and if you use others remember you must provide them free with the design.

Designs look the same

```html
<!DOCTYPE html>
<html lang="en">
<head>
<meta charset="utf-8">
<title>Brellow Quay – The Haven on the Harbour</title>
<link rel="stylesheet" href="https://fonts.googleapis.com/css2?family=Cinzel:wght@400;600;700&family=Lato:wght@400;700&display=swap">
<style>
:root{
  --blue:#2360a6;
  --blue-dark:#1b4f8d;
  --title-blue:#1d4f94;
  --green:#3aa935;
  --green-dark:#2f9a2c;
  --sky:#5d9fdb;
  --ink:#222;
  --muted:#555;
  --panel:#f5f6f8;
  --line:#c9ccd2;
  --white:#fff;
}
*{box-sizing:border-box;margin:0;padding:0}
html,body{width:1200px;height:4594px;overflow:hidden}
body{position:relative;font-family:'Lato',sans-serif;color:var(--ink);background:var(--white)}
.section{position:absolute;left:0;width:1200px;overflow:hidden}
.abs{position:absolute}
.serif{font-family:'Cinzel',serif}
.photo{position:absolute}
.btn{position:absolute;display:flex;align-items:center;justify-content:center;font-size:12px;font-weight:700}
.btn-green{background:var(--green);color:var(--white)}
.btn-outline{border:2px solid var(--green);color:var(--ink);background:var(--white)}
.center-text{left:0;width:1200px;text-align:center}

/* hero */
.hero{top:0;height:576px;background:linear-gradient(180deg,#5c9ddb 0%,#7fb5e6 30%,#9fbfd8 48%,#8c96a4 60%,#b7b3aa 72%,#6c8aa6 84%,#2f5c86 100%)}
.wordmark{font-family:'Cinzel',serif;font-weight:600;letter-spacing:.5px}
.hero .wordmark{left:121px;top:26px;font-size:22px;color:var(--white)}
.nav{left:455px;top:30px}
.nav a{position:absolute;top:0;font-size:11px;color:var(--white);text-decoration:none;white-space:nowrap;transform:translateX(-50%)}
.nav a.active{color:var(--green);border-bottom:1px solid var(--green);padding-bottom:2px}
.contact-btn{left:952px;top:23px;width:127px;height:38px;border:2px solid var(--green);color:var(--white);font-size:12px;gap:6px}
.hero h1{top:132px;font-family:'Cinzel',serif;font-weight:400;font-size:38px;color:var(--white);letter-spacing:1px}
.hero .tagline{top:192px;font-size:12px;letter-spacing:5px;color:var(--white)}
.hero .btn{left:531px;top:234px;width:138px;height:41px}

/* about */
.about{top:576px;height:547px;background:linear-gradient(90deg,#fff 40%,#eef1f5 100%)}
.about .band{left:0;top:0;width:290px;height:547px;background:var(--blue-dark)}
.about .frame{left:285px;top:110px;width:305px;height:373px;border:2px solid var(--green)}
.about .vertical{left:1150px;top:14px;width:46px;height:520px;writing-mode:vertical-rl;font-family:'Cinzel',serif;font-size:44px;color:#dcdfe4;white-space:nowrap;line-height:46px}
.section-title{font-family:'Cinzel',serif;font-weight:400;color:var(--title-blue)}
.about h2{left:662px;top:186px;font-size:32px}
.about .copy{left:662px;top:238px;width:415px;font-size:11.5px;line-height:18px;color:var(--ink)}
.about .copy p{margin-bottom:12px}
.about .btn{left:662px;top:396px;width:155px;height:39px}

/* welcome */
.welcome{top:1123px;height:592px;background:var(--blue)}
.welcome h2{left:121px;top:110px;font-size:35px;line-height:41px;color:var(--white);font-weight:400}
.welcome .copy{left:121px;top:216px;width:430px;font-size:11.5px;line-height:18.5px;color:var(--white)}
.stat{position:absolute;top:384px;width:132px;height:80px;background:var(--green);color:var(--white);text-align:center;padding-top:12px}
.stat b{display:block;font-family:'Cinzel',serif;font-weight:400;font-size:29px;line-height:34px}
.stat span{font-size:11px;font-weight:700}
.welcome .frame{left:637px;top:50px;width:320px;height:425px;border:2px solid var(--green)}

/* services */
.services{top:1715px;height:457px;background:var(--white)}
.services h2{top:34px;font-size:34px}
.lead{font-size:12px;line-height:19px;color:var(--ink)}
.services .lead{top:86px}
.card{position:absolute;background:var(--white);border:1px solid var(--line);box-shadow:5px 5px 0 var(--green)}
.card-inner{position:absolute;inset:0;overflow:hidden}
.card .deco{position:absolute;right:-20px;top:-20px;width:70px;height:70px;border-radius:50%;background:#e6f3e5}
.icon-box{position:absolute;width:36px;height:36px;background:var(--green);display:flex;align-items:center;justify-content:center}
.service-card{top:139px;width:182px;height:277px}
.service-card .icon-box{left:10px;top:18px}
.service-card h3{position:absolute;left:9px;top:68px;font-size:12px;font-weight:700}
.service-card p{position:absolute;left:9px;top:90px;width:160px;font-size:10.5px;line-height:16px;color:var(--ink)}

/* facilities */
.facilities{top:2172px;height:485px;background:var(--panel)}
.facilities h2{top:34px;font-size:34px}
.facilities .lead{top:84px}
.fac-label{position:absolute;width:220px;text-align:center;font-family:'Cinzel',serif;font-weight:600;font-size:16px;color:var(--title-blue)}
.facilities .icon-box{width:43px;height:43px;box-shadow:3px 3px 0 #cfd4da}
.facilities .hub{left:481px;top:283px;width:237px;height:36px;font-family:'Cinzel',serif;font-weight:600;font-size:23px;color:var(--blue);text-align:center}

/* success */
.success{top:2657px;height:552px;background:var(--green)}
.success h2{top:30px;font-size:34px;color:var(--white)}
.success .lead{top:86px;color:var(--white)}
.story{top:157px;width:307px;height:267px;box-shadow:5px 5px 0 var(--blue);border:none}
.story .avatar{left:16px;top:29px;width:55px;height:55px}
.story h3{position:absolute;left:16px;top:104px;font-size:15px;font-weight:700}
.story p{position:absolute;left:16px;top:128px;width:275px;font-size:10.5px;line-height:15.5px;color:var(--ink)}
.story a{position:absolute;left:16px;top:215px;font-size:11px;font-weight:700;color:var(--ink);text-decoration:underline}
.arrow{position:absolute;top:276px}
.success .btn{left:522px;top:474px;width:156px;height:41px;border:2px solid var(--white);color:var(--white);background:transparent;font-weight:400}

/* news */
.news{top:3209px;height:580px;background:var(--panel)}
.news h2{top:32px;font-size:34px;line-height:41px}
.news .btn{left:537px;top:132px;width:126px;height:41px;font-weight:400}
.news-card{top:211px;width:307px;height:330px;box-shadow:5px 5px 0 var(--blue)}
.news-card .thumb{left:0;top:0;width:307px;height:137px}
.date{position:absolute;left:16px;top:128px;height:16px;padding:0 10px;background:var(--green);color:var(--white);font-size:8px;line-height:16px}
.news-card h3{position:absolute;left:16px;top:152px;width:280px;font-family:'Cinzel',serif;font-weight:600;font-size:15px;line-height:20px;color:var(--title-blue)}
.news-card p{position:absolute;left:16px;top:202px;width:278px;font-size:10.5px;line-height:15.5px}
.news-card a{position:absolute;left:16px;top:282px;font-size:11px;font-weight:700;color:var(--ink);text-decoration:underline}

/* cta */
.cta{top:3789px;height:478px;background:var(--blue)}
.cta h2{left:123px;top:108px;font-size:34px;line-height:41px;color:var(--white)}
.cta .copy{left:123px;top:200px;width:380px;font-size:11px;line-height:16.5px;color:var(--white)}
.cta .btn{top:321px;height:39px;font-weight:400}
.cta .partner{left:123px;width:136px;background:var(--white);color:var(--blue);border:2px solid var(--green)}
.cta .consult{left:269px;width:146px;background:transparent;color:var(--white);border:2px solid var(--green)}

/* footer */
.footer{top:4267px;height:327px;background:var(--white)}
.footer .wordmark{left:114px;top:72px;font-size:22px;color:var(--blue)}
.footer .about-text{left:114px;top:138px;width:240px;font-size:10.5px;line-height:15.5px}
.footer .btn{left:114px;top:206px;width:123px;height:40px;font-weight:700}
.footer .divider{left:392px;top:20px;width:1px;height:252px;background:var(--line)}
.col-title{position:absolute;top:66px;font-family:'Cinzel',serif;font-size:16px;color:var(--ink)}
.links{left:551px;top:100px;list-style:none;font-size:11px}
.links li{height:22px;padding-left:12px;position:relative}
.links li::before{content:"";position:absolute;left:0;top:6px;width:4px;height:4px;border-radius:50%;background:var(--ink)}
.contact-item{position:absolute;left:731px;display:flex;gap:10px;font-size:11px;line-height:14px;align-items:flex-start}
.newsletter-text{left:886px;top:96px;width:200px;font-size:10.5px;line-height:15px}
.email{left:886px;top:142px;width:202px;height:29px;border:1px solid var(--line);font-size:8px;color:#999;padding:9px 10px}
.footer .submit{left:886px;top:183px;width:80px;height:27px;font-weight:400;font-size:11px}
.footer .rule{left:0;top:278px;width:1200px;height:1px;background:var(--line)}
.copyright{left:114px;top:293px;font-size:8px}
.social{position:absolute;top:285px;width:28px;height:28px;border-radius:50%;border:1px solid #888}
</style>
</head>
<body>

<!-- Hero -->
<section class="section hero">
  <div class="photo" role="img" aria-label="Harbour skyline of Brellow Quay apartment towers with a cable bridge under blue sky" style="left:0;top:0;width:1200px;height:576px"></div>
  <div class="abs wordmark">BRELLOW QUAY</div>
  <nav class="abs nav">
    <a class="active" style="left:14px">Home</a>
    <a style="left:76px">About Us</a>
    <a style="left:144px">Facilities</a>
    <a style="left:206px">Stratas</a>
    <a style="left:271px">Services</a>
    <a style="left:360px">Local Information</a>
    <a style="left:431px">News</a>
  </nav>
  <div class="btn contact-btn">
    <svg width="14" height="14" viewBox="0 0 24 24" fill="none" stroke="#fff" stroke-width="2"><path d="M22 16.9v3a2 2 0 0 1-2.2 2 19.8 19.8 0 0 1-8.6-3.1 19.5 19.5 0 0 1-6-6A19.8 19.8 0 0 1 2.1 4.2 2 2 0 0 1 4.1 2h3a2 2 0 0 1 2 1.7c.1 1 .4 1.9.7 2.8a2 2 0 0 1-.5 2.1L8 9.9a16 16 0 0 0 6 6l1.3-1.3a2 2 0 0 1 2.1-.4c.9.3 1.8.6 2.8.7a2 2 0 0 1 1.7 2z"/></svg>
    Contact Us
  </div>
  <h1 class="abs center-text">WELCOME TO BRELLOW QUAY</h1>
  <div class="abs center-text tagline">THE HAVEN ON THE HARBOUR</div>
  <div class="btn btn-green">Get a Free Quote</div>
</section>

<!-- About -->
<section class="section about">
  <div class="abs band"></div>
  <div class="photo" role="img" aria-label="Black and white portrait of the estate manager in a suit" style="left:0;top:93px;width:290px;height:454px;background:linear-gradient(180deg,#d9d9d9 0%,#8a8a8a 45%,#2b2b2b 100%)"></div>
  <div class="abs frame"></div>
  <div class="photo" role="img" aria-label="Aerial view of a curved garden walkway among palm trees" style="left:266px;top:94px;width:310px;height:375px;background:linear-gradient(135deg,#3e5a2c 0%,#6f8a4a 40%,#c9c2b0 60%,#4d6b34 100%)"></div>
  <div class="abs vertical">BRELLOW QUAY</div>
  <h2 class="abs section-title">ABOUT US</h2>
  <div class="abs copy">
    <p>Brellow Quay is a community of 2500 residents in more than 1000 apartments, terraces and townhouses on the site of the old Harlow Sugar industrial complex at the northern end of the Harlow Point Peninsula. In addition there are a number of commercial buildings housing several hundred workers.</p>
    <p>The redevelopment of the Harlow Sugar site of over 11 hectares commenced in the early 1990s, and the first residents moved in during 2000. The site is now complete.</p>
  </div>
  <div class="btn btn-outline">Know More About Us</div>
</section>

<!-- Welcome -->
<section class="section welcome">
  <h2 class="abs serif">WELCOME TO BRELLOW<br>QUAY</h2>
  <p class="abs copy">Lorem ipsum dolor sit amet, consectetur adipiscing elit. Vestibulum vel venenatis velit, vehicula fringilla dolor. Phasellus quam turpis, porttitor in volutpat ut, luctus id dolor. Donec hendrerit nulla a ultrices pellentesque. Donec in egestas turpis. Suspendisse in arcu a lacus faucibus posuere. In vitae porta lacus. In nisi ex, consequat et dui sed, luctus dapibus libero. Phasellus dui turpis, interdum sit amet turpis non, volutpat finibus justo. Aenean ut metus convallis, finibus dolor vitae, auctor ligula.</p>
  <div class="stat" style="left:121px"><b>20+</b><span>Sucessful Years</span></div>
  <div class="stat" style="left:267px"><b>2500+</b><span>Residents</span></div>
  <div class="stat" style="left:412px"><b>1000+</b><span>Appartments</span></div>
  <div class="abs frame"></div>
  <div class="photo" role="img" aria-label="Aerial view of landscaped gardens and walkways" style="left:653px;top:38px;width:312px;height:372px;background:linear-gradient(135deg,#3e5a2c 0%,#6f8a4a 40%,#c9c2b0 60%,#4d6b34 100%)"></div>
  <div class="photo" role="img" aria-label="Apartment building behind a large tree by the harbour" style="left:744px;top:328px;width:335px;height:225px;background:linear-gradient(180deg,#4f86c6 0%,#8fb2d6 40%,#4f7a34 70%,#6a6a55 100%)"></div>
</section>

<!-- Services -->
<section class="section services">
  <h2 class="abs center-text section-title" style="color:var(--ink)">OUR SERVICES</h2>
  <p class="abs center-text lead">Lorem ipsum dolor sit amet, consectetur adipiscing elit. Vestibulum vel venenatis velit, vehicula fringilla dolor.<br>Phasellus quam turpis, porttitor in volutpat ut, luctus id dolor.</p>

  <div class="card service-card" style="left:121px">
    <div class="card-inner"><div class="deco"></div></div>
    <div class="icon-box"><svg width="20" height="20" viewBox="0 0 24 24" fill="none" stroke="#fff" stroke-width="1.8"><rect x="4" y="3" width="16" height="18"/><path d="M8 8h8M8 12h8M8 16h5"/></svg></div>
    <h3>Resident Service Manager</h3>
    <p>The Resident Services Manager or RSM is located in the Estate Management office at 45 Carrow Street, on the lower ground floor of Foundry House. RSM services are available 8:00am to 4:30pm Monday to Friday.</p>
  </div>
  <div class="card service-card" style="left:316px">
    <div class="card-inner"><div class="deco"></div></div>
    <div class="icon-box"><svg width="20" height="20" viewBox="0 0 24 24" fill="none" stroke="#fff" stroke-width="1.8"><path d="M3 21h18M5 21V8l7-5 7 5v13M9 21v-6h6v6"/></svg></div>
    <h3>Building Management</h3>
    <p>Each strata makes its own building management arrangements. Some have chosen to retain Crestline Management, and some have engaged Keystone Strata. Both companies have previously managed the whole of Brellow Quay.</p>
  </div>
  <div class="card service-card" style="left:508px">
    <div class="card-inner"><div class="deco"></div></div>
    <div class="icon-box"><svg width="20" height="20" viewBox="0 0 24 24" fill="none" stroke="#fff" stroke-width="1.8"><circle cx="12" cy="7" r="4"/><path d="M4 21c0-4 4-7 8-7s8 3 8 7"/></svg></div>
    <h3>Security</h3>
    <p>Security Security officers are employed by Coastline Guard Services (CGS), the company contracted by the Community Association. CGS is an Australian company with 25 years' experience, and they take pride in the quality of the services they deliver.</p>
  </div>
  <div class="card service-card" style="left:701px">
    <div class="card-inner"><div class="deco"></div></div>
    <div class="icon-box"><svg width="20" height="20" viewBox="0 0 24 24" fill="none" stroke="#fff" stroke-width="1.8"><rect x="3" y="4" width="18" height="14"/><path d="M7 9h10M7 13h6M8 22h8"/></svg></div>
    <h3>Strata Manager</h3>
    <p>Marwick Property Group is contracted by the Community Association to provide strata services for the Community Association and some of the individual strata plans in Brellow Quay.</p>
  </div>
  <div class="card service-card" style="left:893px">
    <div class="card-inner"><div class="deco"></div></div>
    <div class="icon-box"><svg width="20" height="20" viewBox="0 0 24 24" fill="none" stroke="#fff" stroke-width="1.8"><path d="M9 3h6v5H9zM7 8h10l1 13H6z"/></svg></div>
    <h3>Cleaning</h3>
    <p>The Community Association and some strata plans have contracts with Wexley to provide cleaning services. Others have contracted with TidyCab. There is a notebook in each mail room where you can leave notes for your building's cleaner.</p>
  </div>
</section>

<!-- Facilities -->
<section class="section facilities">
  <h2 class="abs center-text section-title">EXPLORE OUR FACILITIES</h2>
  <p class="abs center-text lead">The Community Association owns and manages the following facilities on behalf of all residents and<br>owners in Brellow Quay.</p>
  <svg class="abs" style="left:0;top:0" width="1200" height="485" fill="none" stroke="#9aa0a8" stroke-width="1">
    <path d="M435 219H568V283"/>
    <path d="M765 219H633V283"/>
    <path d="M230 301H481"/>
    <path d="M718 301H966"/>
    <path d="M600 319V378"/>
  </svg>
  <div class="fac-label" style="left:304px;top:168px">Tennis Court</div>
  <div class="icon-box" style="left:392px;top:203px"><svg width="22" height="22" viewBox="0 0 24 24" fill="none" stroke="#fff" stroke-width="1.6"><circle cx="9" cy="9" r="6"/><path d="M13 13l7 7"/></svg></div>
  <div class="fac-label" style="left:676px;top:168px">Harbour Pool</div>
  <div class="icon-box" style="left:765px;top:203px"><svg width="22" height="22" viewBox="0 0 24 24" fill="none" stroke="#fff" stroke-width="1.6"><path d="M2 16c3 0 3 2 6 2s3-2 6-2 3 2 6 2M2 20c3 0 3 2 6 2s3-2 6-2 3 2 6 2M8 14V4h6"/></svg></div>
  <div class="fac-label" style="left:98px;top:250px">Residents' Gym</div>
  <div class="icon-box" style="left:187px;top:280px"><svg width="22" height="22" viewBox="0 0 24 24" fill="none" stroke="#fff" stroke-width="1.6"><path d="M3 21h18M5 21V9h14v12M9 13h2M13 13h2M9 17h2M13 17h2M12 3v6"/></svg></div>
  <div class="fac-label" style="left:878px;top:250px">The Pavilion</div>
  <div class="icon-box" style="left:966px;top:280px"><svg width="22" height="22" viewBox="0 0 24 24" fill="none" stroke="#fff" stroke-width="1.6"><path d="M3 21h18M6 21V6h12v15M9 9h2M13 9h2M9 13h2M13 13h2M11 21v-4h2v4"/></svg></div>
  <div class="abs hub">BRELLOW QUAY</div>
  <div class="icon-box" style="left:579px;top:378px"><svg width="22" height="22" viewBox="0 0 24 24" fill="none" stroke="#fff" stroke-width="1.6"><rect x="4" y="4" width="16" height="12"/><path d="M8 20h8M12 16v4"/></svg></div>
  <div class="fac-label" style="left:490px;top:430px">Function Room</div>
</section>

<!-- Success stories -->
<section class="section success">
  <h2 class="abs center-text serif" style="font-weight:400">OUR SUCESS STORIES</h2>
  <p class="abs center-text lead">The Community Association owns and manages the following facilities on behalf of all residents and<br>owners in Brellow Quay.</p>
  <svg class="arrow" style="left:66px" width="16" height="24" viewBox="0 0 16 24" fill="none" stroke="#111" stroke-width="2.5"><path d="M12 3L4 12l8 9"/></svg>
  <svg class="arrow" style="left:1116px" width="16" height="24" viewBox="0 0 16 24" fill="none" stroke="#111" stroke-width="2.5"><path d="M4 3l8 9-8 9"/></svg>

  <div class="card story" style="left:121px">
    <div class="card-inner"><div class="deco" style="width:110px;height:110px;right:-30px;top:-30px"></div></div>
    <div class="photo avatar" role="img" aria-label="Portrait photo of resident Mara Ellwood" style="background:linear-gradient(135deg,#c9c4bc,#7d7a74)"></div>
    <h3>Mara Ellwood</h3>
    <p>Mara Ellwood travelled to Brellow Quay by the scenic route, overland from Stockholm to Hong Kong, then (following her compatriot Peter Ostrand) working her passage by sea to Sydney.</p>
    <a>View Mara's full story</a>
  </div>
  <div class="card story" style="left:448px">
    <div class="card-inner"><div class="deco" style="width:110px;height:110px;right:-30px;top:-30px"></div></div>
    <div class="photo avatar" role="img" aria-label="Portrait photo of resident Tom Varesi" style="background:linear-gradient(135deg,#b9c3cc,#5f6a74)"></div>
    <h3>Tom Varesi</h3>
    <p>Tom Varesi's grandparents hailed from Odessa and Tipperary. They lived and laboured in Harlow Point, Kellow and the City, as working class immigrants making their way in a new world.</p>
    <a>View Tom's full story</a>
  </div>
  <div class="card story" style="left:774px">
    <div class="card-inner"><div class="deco" style="width:110px;height:110px;right:-30px;top:-30px"></div></div>
    <div class="photo avatar" role="img" aria-label="Portrait photo of resident Ruth Kellaway" style="background:linear-gradient(135deg,#d8b9a8,#a0564a)"></div>
    <h3>Ruth Kellaway</h3>
    <p>Ruth Kellaway enjoyed an exceptional career in banking and retired as a Senior Executive of the Meridian Bank after working creatively in all its specialist divisions.</p>
    <a>View Ruth's full story</a>
  </div>
  <div class="btn">View All Sucess Stories</div>
</section>

<!-- News -->
<section class="section news">
  <h2 class="abs center-text section-title">THE LATEST NEWS FROM<br>BRELLOW QUAY</h2>
  <div class="btn btn-green">View All News</div>

  <div class="card news-card" style="left:121px">
    <div class="photo thumb" role="img" aria-label="Christmas concert with a performer in a Santa costume on stage" style="background:linear-gradient(135deg,#5a1a14,#b5342a 50%,#2c2420)"></div>
    <div class="date">Nov 14, 2022</div>
    <h3>Christmas in Harlow Point is Happening.</h3>
    <p>Rain, hail or shine! Come to the Harbourside Sporting Complex Sunday, 27 November 11.30 am – 5.30 pm Market stalls, food stalls, live entertainment, kids' activities, Santa Buy your raffle tickets online now..</p>
    <a>Read More</a>
  </div>
  <div class="card news-card" style="left:448px">
    <div class="photo thumb" role="img" aria-label="Brick community hall building under a blue sky" style="background:linear-gradient(180deg,#5c8fcf 0%,#9ab8d8 35%,#8a4a2c 60%,#5a3220 100%)"></div>
    <div class="date">Mar 13, 2023</div>
    <h3>Voting information for Harlow Point residents.</h3>
    <p>As the Harlow Point Civic Hall is currently closed for renovations, voting for the forthcoming State election will be held at Larkin House Pier Wharf. Pre-polling at LARKIN HOUSE Pier Wharf, Tessel Rd...</p>
    <a>Read More</a>
  </div>
  <div class="card news-card" style="left:774px">
    <div class="photo thumb" role="img" aria-label="Cleaners in high visibility clothing sorting recycling by the water" style="background:linear-gradient(135deg,#3c6a9e,#d9782e 45%,#5a7a3a 80%)"></div>
    <div class="date">Aug 2, 2023</div>
    <h3>Be kind to your cleaner</h3>
    <p>Some residents are careless depositing their recycling in the garbage room. Please follow the signs for what goes where – and NO plastic bags or polystyrene! Flatten cardboard boxes to make room for more, and it is easy for one resident to do...</p>
    <a>Read More</a>
  </div>
</section>

<!-- Call to action -->
<section class="section cta">
  <div class="photo" role="img" aria-label="Residents relaxing on a waterfront lawn below apartment towers" style="left:599px;top:0;width:601px;height:478px;background:linear-gradient(180deg,#3f7ec6 0%,#8fb6dc 35%,#b89a6a 55%,#5a7a3a 75%,#3d5e2c 100%)"></div>
  <h2 class="abs serif" style="font-weight:400">LET'S BUILD A BETTER<br>FUTURE TOGETHER</h2>
  <p class="abs copy">Investing in your future has never been easier. With Brellow Quay, you're not just buying a house; you're securing your family's future. Our homes are built to last, appreciate in value, and provide you with the comfort you deserve. Your dream home is more than just bricks and mortar; it's an investment in your future legacy.</p>
  <div class="btn partner">Partner With Us</div>
  <div class="btn consult">Book a Consultation</div>
</section>

<!-- Footer -->
<footer class="section footer">
  <div class="abs wordmark">BRELLOW QUAY</div>
  <p class="abs about-text">Brellow Quay is managed by the Brellow Quay Community Association (CA) and the Owners' Corporation of each strata plan.</p>
  <div class="btn btn-outline">View Gallery</div>
  <div class="abs divider"></div>

  <div class="col-title" style="left:551px">Quick Links</div>
  <ul class="abs links">
    <li>Home</li><li>About Us</li><li>Facilities</li><li>Stratas</li><li>Services</li><li>Local Information</li><li>News</li>
  </ul>

  <div class="col-title" style="left:731px">Contact Us</div>
  <div class="contact-item" style="top:102px">
    <svg width="14" height="18" viewBox="0 0 24 24" fill="none" stroke="#3aa935" stroke-width="2"><path d="M12 22s7-7 7-12a7 7 0 0 0-14 0c0 5 7 12 7 12z"/><circle cx="12" cy="10" r="2.5"/></svg>
    <span>Lorem ipsum dolor<br>sit amet, consecte-<br>tur adipiscing</span>
  </div>
  <div class="contact-item" style="top:158px">
    <svg width="16" height="16" viewBox="0 0 24 24" fill="none" stroke="#3aa935" stroke-width="2"><path d="M22 16.9v3a2 2 0 0 1-2.2 2 19.8 19.8 0 0 1-8.6-3.1 19.5 19.5 0 0 1-6-6A19.8 19.8 0 0 1 2.1 4.2 2 2 0 0 1 4.1 2h3a2 2 0 0 1 2 1.7c.1 1 .4 1.9.7 2.8a2 2 0 0 1-.5 2.1L8 9.9a16 16 0 0 0 6 6l1.3-1.3a2 2 0 0 1 2.1-.4c.9.3 1.8.6 2.8.7a2 2 0 0 1 1.7 2z"/></svg>
    <span>+123-456-7890</span>
  </div>
  <div class="contact-item" style="top:200px;align-items:center">
    <svg width="14" height="20" viewBox="0 0 16 24" fill="none" stroke="#3aa935" stroke-width="2"><rect x="2" y="1" width="12" height="22" rx="2"/><path d="M6 19h4"/></svg>
    <span>000-0000-000</span>
  </div>

  <div class="col-title" style="left:886px">Newsletter</div>
  <p class="abs newsletter-text">Stay in the Loop with Our Latest Development updates.</p>
  <div class="abs email">Email Address</div>
  <div class="btn btn-green submit">Submit</div>

  <div class="abs rule"></div>
  <div class="abs copyright">© 2023 Brellow Quay. All Right Reserved.</div>
  <div class="social" style="left:986px"></div>
  <div class="social" style="left:1022px"></div>
  <div class="social" style="left:1058px"></div>
</footer>

</body>
</html>
```